Badge Graphics

We are creating an internal directory/org chart here within our intranet at Brevant and plan to incorporate "badges". Badges will represent different awards people have won, years of service, etc. This is a fun way to have people's achievements available for all to see.
We need some interesting fun graphics to go along with our badges. Badges need to be 300 pixels wide by 50 pixels high. Badge/Graphic needs to include the actual badge name so it should say "Bravostar" and have the graphic either next to it or around it. Please have consistent font for all awards.
Badges needed are:
Bravostar
Saltine Cracker Challenge Winner
Talent Show Winner
Bravvy
WOW #1
Grinder Award - one note for clarification, this is actual meat grinder
Employee Referrer
Top Employee Referrer
Years of Service 5 years
Years of Service 10 years
Years of Service 15 years
This is for internal use only so should be fun and bold. Does not need to be tied to our Brevant Brand. This is separate from our external branding and just for internal use of employees looking at our org chart.
Employee
- Calibri

```html
<!DOCTYPE html>
<html lang="en">
<head>
<meta charset="utf-8">
<title>Badge Graphics</title>
<link rel="stylesheet" href="https://fonts.googleapis.com/css2?family=Carlito:wght@700&display=swap">
<style>
  :root {
    --canvas-bg: #474747;
    --frame: #ffffff;
    --ink: #111111;
    --star-start: #d2e5a0;
    --star-end: #eef5e6;
    --cracker-start: #7ccfdc;
    --cracker-end: #d8eff3;
    --talent-start: #a8b3dd;
    --talent-end: #e6e8f3;
    --red: #e8202e;
    --orange: #f7923a;
    --yellow: #e3d200;
    --salmon: #f26a6a;
    --cream: #ffff9a;
  }
  * { margin: 0; padding: 0; box-sizing: border-box; }
  html, body {
    width: 1200px;
    height: 1000px;
    overflow: hidden;
    background: var(--canvas-bg);
  }
  .badge-sheet {
    position: relative;
    width: 1200px;
    height: 1000px;
    font-family: "Carlito", "Calibri", sans-serif;
    font-weight: 700;
  }
  .badge {
    position: absolute;
    left: 128px;
    width: 942px;
    border: 4px solid var(--frame);
    border-radius: 2px;
  }
  .badge--bravostar { top: 128px; height: 158px; background: linear-gradient(90deg, var(--star-start), var(--star-end)); }
  .badge--cracker { top: 403px; height: 155px; background: linear-gradient(90deg, var(--cracker-start), var(--cracker-end)); }
  .badge--talent { top: 670px; height: 159px; background: linear-gradient(90deg, var(--talent-start), var(--talent-end)); }

  .badge__title {
    position: absolute;
    left: 0;
    width: 650px;
    text-align: center;
    line-height: 1;
    -webkit-text-stroke: 8px var(--ink);
    paint-order: stroke fill;
    letter-spacing: 0.5px;
  }
  .badge--bravostar .badge__title { top: 22px; font-size: 92px; color: var(--red); }
  .badge--cracker .badge__title { top: 18px; font-size: 58px; line-height: 60px; }
  .badge--talent .badge__title { top: 20px; font-size: 62px; line-height: 63px; }
  .line { display: block; }
  .line--orange { color: var(--orange); }
  .line--yellow { color: var(--yellow); }
  .line--salmon { color: var(--salmon); }
  .line--cream { color: var(--cream); }

  .badge__art {
    position: absolute;
    border-radius: 6px;
  }
  .badge--bravostar .badge__art {
    left: 605px; top: 10px; width: 318px; height: 140px;
    background: linear-gradient(180deg, rgba(240,200,80,0.35), rgba(220,40,50,0.35));
  }
  .badge--cracker .badge__art {
    left: 678px; top: 8px; width: 188px; height: 140px;
    background: linear-gradient(180deg, rgba(230,120,60,0.3), rgba(20,20,20,0.35));
  }
  .badge--talent .badge__art {
    left: 640px; top: 6px; width: 285px; height: 148px;
    background: linear-gradient(180deg, rgba(240,160,180,0.35), rgba(190,40,20,0.3));
  }
</style>
</head>
<body>
  <main class="badge-sheet">
    <section class="badge badge--bravostar">
      <h2 class="badge__title">Bravostar</h2>
      <div class="badge__art" role="img" aria-label="Cartoon kids on a red carpet between velvet ropes and shooting stars"></div>
    </section>

    <section class="badge badge--cracker">
      <h2 class="badge__title">
        <span class="line line--orange">Saltine Cracker</span>
        <span class="line line--yellow">Challenge Winner</span>
      </h2>
      <div class="badge__art" role="img" aria-label="Cartoon kid holding a trophy on a winners' podium with two other kids and confetti"></div>
    </section>

    <section class="badge badge--talent">
      <h2 class="badge__title">
        <span class="line line--salmon">Talent Show</span>
        <span class="line line--cream">Winner</span>
      </h2>
      <div class="badge__art" role="img" aria-label="Cartoon ballerina and guitar player performing on a stage under spotlights"></div>
    </section>
  </main>
</body>
</html>
```